Rimah Advertising & Publicity business cards

I would like my Company's business card to be designed creatively & profissionally the logo is attached in both Arabic & english and prefer to have my emblem dimmed on the card as well
-Logo ( Arabic & English)
-Name (Arabic & English)
-Title ( Arabic & English)
-----------
-Location
-rimahads (icon)
-Mobile phone (icon)
-Email (icon)
-Instagram (icon)
-WhatsApp (icon)

Target Market(s)

Industry/Entity Type

Marketing

Contact Information for Business Card

-Logo ( Arabic & English)
-Name (Arabic & English)
-----------
-Location
-rimahads (icon)
-Mobile phone (icon)
-Email (icon)
-Instagram (icon)
-WhatsApp (icon)

Font styles to use
Serif

Requirements
Must have
• all what is mentions in business card details blanked and i will add the data my self
Nice to have
• Dim emblem on my business card both Arabic & english

```html
<!DOCTYPE html>
<html lang="en">
<head>
<meta charset="utf-8">
<title>Rimah Advertising &amp; Publicity – Business Cards</title>
<link rel="stylesheet" href="https://fonts.googleapis.com/css2?family=Cairo:wght@400;700&family=Didact+Gothic&display=swap">
<style>
  :root {
    --page: #ffffff;
    --card: #ffffff;
    --ink: #111111;
    --muted: #555555;
    --teal: #3fbfbc;
    --teal-pale: #a9dedb;
    --shadow: rgba(0,0,0,0.28);
  }
  * { margin: 0; padding: 0; box-sizing: border-box; }
  html, body { width: 1013px; height: 1200px; overflow: hidden; background: var(--page); }
  .sheet { position: relative; width: 1013px; height: 1200px; }
  .card {
    position: absolute; left: 45px; width: 922px; height: 512px;
    background: var(--card); overflow: hidden;
    box-shadow: 0 3px 14px var(--shadow);
  }
  .card--arabic { top: 54px; direction: rtl; }
  .card--english { top: 631px; }
  .decor { position: absolute; }
  .emblem-mark {
    position: absolute; width: 110px; height: 110px; background: var(--teal);
  }
  .divider { position: absolute; width: 2px; background: var(--ink); }

  /* Arabic card */
  .card--arabic .decor--large { left: 673px; top: 18px; width: 249px; height: 480px; }
  .card--arabic .decor--small { left: 0; top: 221px; width: 68px; height: 72px; }
  .card--arabic .emblem-mark { left: 563px; top: 200px; }
  .card--arabic .divider { left: 482px; top: 178px; height: 150px; }
  .ar-block { position: absolute; right: 448px; top: 160px; text-align: right; font-family: "Cairo", sans-serif; }
  .ar-wordmark { font-size: 84px; font-weight: 700; line-height: 1.1; color: var(--ink); }
  .ar-tagline { font-size: 22px; font-weight: 700; line-height: 1.4; margin-top: 4px; color: var(--ink); }
  .ar-person { font-size: 22px; font-weight: 700; line-height: 1.3; color: var(--ink); }
  .ar-person .title { color: var(--teal); }
  .ar-contacts { list-style: none; margin-top: 4px; font-size: 19px; line-height: 22px; color: var(--muted); }
  .ar-contacts li { display: flex; align-items: center; gap: 6px; }
  .ar-contacts .latin { font-family: "Didact Gothic", sans-serif; direction: ltr; }

  /* English card */
  .card--english .decor--large { left: 0; top: 15px; width: 240px; height: 497px; }
  .card--english .decor--small { left: 848px; top: 218px; width: 74px; height: 85px; }
  .card--english .emblem-mark { left: 285px; top: 197px; }
  .card--english .divider { left: 435px; top: 188px; height: 115px; }
  .en-block { position: absolute; left: 462px; top: 160px; font-family: "Didact Gothic", sans-serif; color: var(--ink); }
  .en-wordmark { font-size: 96px; line-height: 1.1; letter-spacing: 1px; }
  .en-tagline { font-size: 26px; line-height: 1.3; margin-top: 4px; }
  .en-person { font-size: 20px; font-weight: 700; font-family: "Cairo", sans-serif; line-height: 1.4; }
  .en-person .title { color: var(--teal); font-weight: 400; font-family: "Didact Gothic", sans-serif; }
  .en-contacts { list-style: none; margin-top: 10px; font-size: 22px; line-height: 22px; color: var(--muted); }
  .en-contacts li { display: flex; align-items: center; gap: 6px; }

  .icon { width: 16px; height: 16px; flex: none; }
</style>
</head>
<body>
<main class="sheet">

  <section class="card card--arabic" aria-label="Rimah business card, Arabic side">
    <svg class="decor decor--large" viewBox="0 0 249 480" role="img" aria-label="Faded brand emblem ornament">
      <polygon points="0,240 249,0 249,480" fill="var(--teal-pale)"/>
    </svg>
    <svg class="decor decor--small" viewBox="0 0 68 72" role="img" aria-label="Faded brand emblem ornament">
      <polygon points="0,0 68,36 0,72" fill="var(--teal-pale)"/>
    </svg>
    <div class="emblem-mark" aria-hidden="true"></div>
    <div class="divider"></div>
    <div class="ar-block">
      <div class="ar-wordmark">رماح</div>
      <div class="ar-tagline">للدعاية والإعلان</div>
      <div class="ar-person">كريم حداد <span class="title">المالك</span></div>
      <ul class="ar-contacts">
        <li><svg class="icon" viewBox="0 0 16 16"><path d="M3 1l3 3-2 2c1 2 3 4 5 5l2-2 3 3-2 3C7 15 1 9 1 3z" fill="var(--ink)"/></svg><span>+ ٩٦١ ٩ ٤٢٠ ٣١٨</span></li>
        <li><svg class="icon" viewBox="0 0 16 16"><rect x="4" y="1" width="8" height="14" rx="1" fill="var(--ink)"/><rect x="5.5" y="3" width="5" height="5" fill="#fff"/></svg><span>+ ٩٦١ ٣ ٥١٢ ٥١٢</span></li>
        <li><svg class="icon" viewBox="0 0 16 16"><circle cx="8" cy="8" r="7" fill="var(--ink)"/></svg><span>+ ٩٦١ ٣ ٥١٢ ٥١٢</span></li>
        <li><svg class="icon" viewBox="0 0 16 16"><rect x="1" y="4" width="14" height="10" fill="var(--ink)"/><path d="M1 4l7 5 7-5" stroke="#fff" fill="none"/></svg><span class="latin">www.rimah-ads.com :</span></li>
        <li><svg class="icon" viewBox="0 0 16 16"><rect x="1" y="1" width="14" height="14" rx="3" fill="var(--ink)"/></svg><span class="latin">rimahads:</span></li>
      </ul>
    </div>
  </section>

  <section class="card card--english" aria-label="Rimah business card, English side">
    <svg class="decor decor--large" viewBox="0 0 240 497" role="img" aria-label="Faded brand emblem ornament">
      <polygon points="0,0 240,248 0,497" fill="var(--teal-pale)"/>
    </svg>
    <svg class="decor decor--small" viewBox="0 0 74 85" role="img" aria-label="Faded brand emblem ornament">
      <polygon points="74,0 0,42 74,85" fill="var(--teal-pale)"/>
    </svg>
    <div class="emblem-mark" aria-hidden="true"></div>
    <div class="divider"></div>
    <div class="en-block">
      <div class="en-wordmark">Rimah</div>
      <div class="en-tagline">Advertising and Publicity</div>
      <div class="en-person">Karim Haddad <span class="title">Owner</span></div>
      <ul class="en-contacts">
        <li><svg class="icon" viewBox="0 0 16 16"><path d="M3 1l3 3-2 2c1 2 3 4 5 5l2-2 3 3-2 3C7 15 1 9 1 3z" fill="var(--ink)"/></svg><span>: + 961 9 420 318</span></li>
        <li><svg class="icon" viewBox="0 0 16 16"><rect x="4" y="1" width="8" height="14" rx="1" fill="var(--ink)"/><rect x="5.5" y="3" width="5" height="5" fill="#fff"/></svg><span>: + 961 3 512 512</span></li>
        <li><svg class="icon" viewBox="0 0 16 16"><circle cx="8" cy="8" r="7" fill="var(--ink)"/></svg><span>: + 961 3 512 512</span></li>
        <li><svg class="icon" viewBox="0 0 16 16"><rect x="1" y="4" width="14" height="10" fill="var(--ink)"/><path d="M1 4l7 5 7-5" stroke="#fff" fill="none"/></svg><span>: www.rimah-ads.com</span></li>
        <li><svg class="icon" viewBox="0 0 16 16"><rect x="1" y="1" width="14" height="14" rx="3" fill="var(--ink)"/></svg><span>: rimahads</span></li>
      </ul>
    </div>
  </section>

</main>
</body>
</html>
```